Bathroom Renovation Business card design needed

Bathroom, Kitchen & Laundry Renovations
Mainly complete bathroom renovations

Target Market(s)

people wanting a total bathroom renovations and other trades people

Industry/Entity Type

Business

Contact Information for Business Card

Holt Bathrooms
Dara Holt
Mobile: 0487 226504
Licence no: 604519K
Email: holtbathrooms@postlane.net

Logo styles of interest
Lettermark Logo
Requirements
Must have
• the business card should be predominantly blue
Nice to have
• the HB logo featured in the business card will be used on tshirts,tax invoices , letters etc so the HB will be the main feature, and preferably blue
Should not have
• We found the red HB logo through google images. We understand that it cannot be exactly the same but we like how the HB is linked. The example business card is something we designed but we prefer more blues. Maybe different shades of blue.

```html
<!DOCTYPE html>
<html lang="en">
<head>
<meta charset="utf-8">
<title>Holt Bathrooms – Business Card</title>
<link rel="stylesheet" href="https://fonts.googleapis.com/css2?family=Arimo:wght@400;700&family=Righteous&display=swap">
<style>
  :root {
    --card-blue: #3d7cc3;
    --card-blue-light: #4686cc;
    --mark-blue: #1657a6;
    --name-white: #ffffff;
    --detail-blue: #c9dcf3;
    --shadow-dark: rgba(10, 30, 70, 0.75);
  }
  html, body {
    margin: 0;
    padding: 0;
    width: 1200px;
    height: 693px;
    overflow: hidden;
    background: #ffffff;
  }
  .card {
    position: relative;
    width: 1200px;
    height: 693px;
    background: radial-gradient(ellipse at 50% 45%, var(--card-blue-light), var(--card-blue) 75%);
    font-family: "Arimo", Arial, sans-serif;
    text-align: center;
    overflow: hidden;
  }
  .brand-mark {
    position: absolute;
    top: 104px;
    left: 0;
    width: 100%;
    font-family: "Righteous", sans-serif;
    font-size: 118px;
    line-height: 1;
    color: var(--mark-blue);
    letter-spacing: 4px;
  }
  .business-name {
    position: absolute;
    top: 262px;
    left: 0;
    width: 100%;
    margin: 0;
    font-family: "Righteous", sans-serif;
    font-weight: 400;
    font-size: 64px;
    line-height: 1;
    color: var(--name-white);
    text-shadow: 3px 4px 3px var(--shadow-dark);
    letter-spacing: 1px;
  }
  .owner-name {
    position: absolute;
    top: 352px;
    left: 0;
    width: 100%;
    margin: 0;
    font-weight: 400;
    font-size: 60px;
    line-height: 1;
    color: var(--name-white);
    text-shadow: 2px 3px 3px var(--shadow-dark);
  }
  .contact-line {
    position: absolute;
    left: 0;
    width: 100%;
    margin: 0;
    font-size: 37px;
    line-height: 1;
    color: var(--detail-blue);
  }
  .contact-mobile { top: 450px; }
  .contact-email { top: 516px; }
  .contact-licence { top: 577px; }
</style>
</head>
<body>
  <main class="card">
    <div class="brand-mark">HB</div>
    <h1 class="business-name">Holt Bathrooms</h1>
    <h2 class="owner-name">Dara Holt</h2>
    <p class="contact-line contact-mobile">Mobile: 0487 226504</p>
    <p class="contact-line contact-email">Email: holtbathrooms@postlane.net</p>
    <p class="contact-line contact-licence">Licence no: 604519K</p>
  </main>
</body>
</html>
```